Business Cards

I'd like help creating business cards with the full logo "Veltrona Capital Partners" on the back of the card (navy background with white writing), and abbreviated logo "VCP" on the front. Would like to list name, title, phone number, email, and website listed on front of card. Would like to keep very simple. Front font Arial or similar.

```html
<!DOCTYPE html>
<html lang="en">
<head>
<meta charset="utf-8">
<title>Veltrona Capital Partners – Business Cards</title>
<link href="https://fonts.googleapis.com/css2?family=Arimo:wght@400;700&display=swap" rel="stylesheet">
<style>
  :root {
    --navy: #1f3a73;
    --navy-deep: #1a3266;
    --paper: #ffffff;
    --ink: #111111;
    --backdrop: #222222;
  }
  * { box-sizing: border-box; margin: 0; padding: 0; }
  html, body { width: 1200px; height: 780px; overflow: hidden; }
  body {
    background: var(--backdrop);
    font-family: "Arimo", Arial, sans-serif;
    display: flex;
    align-items: center;
    justify-content: center;
    gap: 40px;
  }
  .card {
    position: relative;
    width: 540px;
    height: 308px;
    overflow: hidden;
  }

  /* Front */
  .card-front { background: var(--paper); }
  .edge-bar {
    position: absolute;
    width: 15px;
    background: var(--navy);
  }
  .edge-bar-left { left: 0; top: 68px; height: 160px; }
  .edge-bar-right { right: 0; top: 48px; height: 156px; }
  .monogram {
    position: absolute;
    left: 44px;
    top: 0;
    width: 210px;
    height: 308px;
    display: flex;
    align-items: center;
    justify-content: center;
    color: var(--navy);
    font-weight: 700;
    font-size: 76px;
    letter-spacing: 1px;
  }
  .divider {
    position: absolute;
    left: 266px;
    top: 70px;
    width: 1.5px;
    height: 170px;
    background: linear-gradient(to bottom, transparent, var(--ink) 20%, var(--ink) 80%, transparent);
  }
  .details {
    position: absolute;
    left: 290px;
    top: 84px;
    right: 20px;
  }
  .person-name {
    color: var(--navy);
    font-weight: 700;
    font-size: 30px;
    line-height: 1;
    letter-spacing: -0.3px;
    white-space: nowrap;
  }
  .person-title {
    color: var(--ink);
    font-size: 12.5px;
    margin-top: 6px;
  }
  .contact-list {
    list-style: none;
    margin-top: 22px;
  }
  .contact-item {
    display: flex;
    align-items: center;
    gap: 8px;
    font-size: 12.5px;
    color: var(--ink);
    line-height: 1;
    margin-bottom: 7px;
  }
  .contact-icon { width: 13px; height: 13px; flex: none; }

  /* Back */
  .card-back { background: var(--navy-deep); }
  .back-pattern {
    position: absolute;
    inset: 0;
    background: linear-gradient(135deg, #1c3670 0%, #1f3a73 50%, #1a3163 100%);
  }
  .back-wordmark {
    position: absolute;
    left: 50%;
    top: 50%;
    transform: translate(-50%, -50%);
    color: var(--paper);
    font-weight: 700;
    font-size: 17px;
    letter-spacing: 1.5px;
    white-space: nowrap;
  }
</style>
</head>
<body>

  <section class="card card-front" aria-label="Business card front">
    <div class="edge-bar edge-bar-left"></div>
    <div class="edge-bar edge-bar-right"></div>

    <div class="monogram">VCP</div>
    <div class="divider"></div>

    <div class="details">
      <h1 class="person-name">Dean Halvorsen</h1>
      <p class="person-title">Co-Founder and Managing Partner</p>

      <ul class="contact-list">
        <li class="contact-item">
          <svg class="contact-icon" viewBox="0 0 24 24" aria-hidden="true">
            <path fill="#1f3a73" d="M6.6 10.8a15.1 15.1 0 0 0 6.6 6.6l2.2-2.2a1 1 0 0 1 1-.25 11.4 11.4 0 0 0 3.6.57 1 1 0 0 1 1 1V20a1 1 0 0 1-1 1A17 17 0 0 1 3 4a1 1 0 0 1 1-1h3.5a1 1 0 0 1 1 1c0 1.25.2 2.45.57 3.57a1 1 0 0 1-.25 1z"/>
          </svg>
          (555) 214-3390
        </li>
        <li class="contact-item">
          <svg class="contact-icon" viewBox="0 0 24 24" aria-hidden="true">
            <circle cx="12" cy="12" r="10" fill="#1f3a73"/>
            <path fill="none" stroke="#fff" stroke-width="1.4" d="M2 12h20M12 2c3 3 3 17 0 20M12 2c-3 3-3 17 0 20"/>
          </svg>
          www.veltronacp.com
        </li>
        <li class="contact-item">
          <svg class="contact-icon" viewBox="0 0 24 24" aria-hidden="true">
            <rect x="2" y="5" width="20" height="14" rx="1.5" fill="#1f3a73"/>
            <path fill="none" stroke="#fff" stroke-width="1.6" d="M3 6.5l9 6.5 9-6.5"/>
          </svg>
          Dean.Halvorsen@VeltronaCP.com
        </li>
      </ul>
    </div>
  </section>

  <section class="card card-back" aria-label="Business card back">
    <div class="back-pattern" role="img" aria-label="Tone-on-tone navy embossed pattern of the repeated company name"></div>
    <div class="back-wordmark">VELTRONA CAPITAL PARTNERS</div>
  </section>

</body>
</html>
```